Meadowlark Dental Letterhead

Please design full color letterhead for meadowlark dental. Letterhead should match the motif of the business card. Print and logo should be confined to a one inch margin on top and bottom. The following info should be included:
Meadowlrk Dental with the tooth logo
Curtis R. Holloway, DDS
Gentle Hands, Bright Smiles Daily
Phone #: 918.555.0147
Address: 24813-C N Sycamore, Bixby, OK

```html
<!DOCTYPE html>
<html lang="en">
<head>
<meta charset="utf-8">
<title>Meadowlark Dental Letterhead</title>
<link href="https://fonts.googleapis.com/css2?family=Montserrat:wght@400;500;600;700&display=swap" rel="stylesheet">
<style>
  :root {
    --backdrop: #8a8a8a;
    --paper: #ffffff;
    --ink: #3a3d42;
    --brand-blue: #1f5fae;
    --brand-red: #e8412c;
    --brand-green: #4db848;
    --watermark: #eceded;
  }
  * { box-sizing: border-box; margin: 0; padding: 0; }
  html, body {
    width: 1200px; height: 1000px; overflow: hidden;
    background: var(--backdrop);
    font-family: "Montserrat", sans-serif;
  }
  .letterhead {
    position: absolute; left: 237px; top: 30px;
    width: 726px; height: 940px;
    background: var(--paper);
    box-shadow: 0 4px 14px rgba(0,0,0,.35);
    overflow: hidden;
  }
  .brand {
    position: absolute; left: 46px; top: 48px;
    display: flex; align-items: center; gap: 12px;
  }
  .brand-mark {
    width: 42px; height: 42px; border-radius: 6px;
    background: var(--brand-blue);
  }
  .brand-name {
    font-size: 22px; font-weight: 600; line-height: 1.05;
    letter-spacing: 1px; color: var(--brand-blue);
    text-transform: uppercase;
  }
  .practice-info {
    position: absolute; right: 36px; top: 58px;
    display: flex; gap: 10px; align-items: stretch;
  }
  .practice-id { text-align: right; }
  .tagline {
    font-size: 8px; font-weight: 600; color: var(--ink);
    text-transform: uppercase; letter-spacing: .2px;
  }
  .doctor {
    font-size: 12.5px; font-weight: 700; color: var(--brand-blue);
    margin-top: 3px;
  }
  .divider { display: flex; gap: 2px; }
  .divider span { width: 2px; }
  .divider .r { background: var(--brand-red); }
  .divider .b { background: var(--brand-blue); }
  .divider .g { background: var(--brand-green); }
  .contact { font-size: 11px; color: var(--ink); line-height: 1.4; }
  .contact div { display: flex; align-items: center; gap: 5px; }
  .contact .phone { font-size: 12px; }
  .contact svg { width: 9px; height: 9px; fill: var(--brand-blue); }
  .watermark {
    position: absolute; left: 0; top: 450px; width: 726px;
    text-align: center; font-size: 44px; font-weight: 600;
    letter-spacing: 2px; line-height: 1.1; color: var(--watermark);
    text-transform: uppercase;
  }
  .footer-band {
    position: absolute; left: 0; bottom: 0;
    width: 726px; height: 28px;
    background: var(--brand-green);
  }
  .address {
    position: absolute; right: 40px; bottom: 6px;
    font-size: 11.5px; color: var(--paper); letter-spacing: .2px;
  }
</style>
</head>
<body>
  <div class="letterhead">
    <div class="brand">
      <div class="brand-mark"></div>
      <div class="brand-name">Meadowlark<br>Dental</div>
    </div>

    <div class="practice-info">
      <div class="practice-id">
        <div class="tagline">Gentle Hands, Bright Smiles Daily</div>
        <div class="doctor">Curtis R. Holloway, DDS</div>
      </div>
      <div class="divider"><span class="r"></span><span class="b"></span><span class="g"></span></div>
      <div class="contact">
        <div class="phone"><svg viewBox="0 0 10 10"><path d="M1 3c0-1 1-2 4-2s4 1 4 2v1H7V3H3v1H1z M2 5h6l1 4H1z"/></svg>918.555.0147</div>
        <div><svg viewBox="0 0 10 10"><circle cx="5" cy="5" r="4.5"/></svg>www.meadowlarkdentalok.com</div>
      </div>
    </div>

    <div class="watermark" aria-hidden="true">Meadowlark<br>Dental</div>

    <div class="footer-band"></div>
    <div class="address">24813-C North Sycamore, Bixby, OK 74008</div>
  </div>
</body>
</html>
```